TRAVo Kiosk Webpage Design

Just need a simple, single page web design. I have a preliminary idea of what I need, just want to add a professional touch to it. We already have the google map locator plug-in. Generic website is already up and I can send the locator plugin when project is complete for final HTML/CSS Coding. Needs to be coded as a responsive design on a flexible grid (i.e. will auto adjust screen for desktop/tablet/mobile devices)
Target Market(s)
Business/Student/General Public, Mobile Office Kiosk Rental Station (Technology-Printing-Scanning-Faxing, etc...)
Industry/Entity Type
It Professional
Coding
Coded - Design and coding required
Number of Pages Required
1 page
Look and feel
Each slider illustrates characteristics of the customer's brand and the style your logo design should communicate.

```html
<!DOCTYPE html>
<html lang="en">
<head>
<meta charset="utf-8">
<title>TRAVo Kiosk</title>
<link href="https://fonts.googleapis.com/css2?family=Roboto:wght@300;400;500;700&display=swap" rel="stylesheet">
<style>
:root{
  --blue:#1e88d0;
  --blue-dark:#166fae;
  --blue-light:#2ea0e4;
  --ink:#2b2b2b;
  --text:#666;
  --muted:#999;
  --line:#e3e3e3;
  --soft:#f4f4f4;
  --band:#e9e9e9;
  --footer:#222;
  --white:#fff;
}
*{box-sizing:border-box;margin:0;padding:0}
html,body{width:1200px;height:2832px;overflow:hidden}
body{font-family:"Roboto",Arial,sans-serif;color:var(--text);background:var(--white);position:relative}
a{color:inherit;text-decoration:none}

/* header */
.site-header{position:absolute;top:0;left:0;width:1200px;height:152px;background:var(--white)}
.brand{position:absolute;left:112px;top:30px;display:flex;align-items:center;gap:14px}
.brand-square{width:44px;height:44px;background:var(--blue)}
.brand-name{font-size:40px;font-weight:700;color:var(--ink);letter-spacing:1px}
.contact-bar{position:absolute;right:108px;top:22px;display:flex;gap:28px;font-size:14px;color:var(--text)}
.contact-bar span{display:flex;align-items:center;gap:8px}
.contact-bar b{color:var(--blue);font-weight:500}
.main-nav{position:absolute;right:100px;top:76px;display:flex}
.main-nav a{font-size:15px;color:var(--text);padding:12px 26px;border-left:1px solid var(--line);text-transform:uppercase;letter-spacing:.5px}
.main-nav a:first-child{border-left:none}
.main-nav a.active{background:var(--blue);color:var(--white)}

/* hero */
.hero{position:absolute;top:152px;left:0;width:1200px;height:508px;background:linear-gradient(90deg,#f2f5f8 0%,#e5ecf2 45%,#dfe7ee 100%);overflow:hidden}
.hero-photo{position:absolute;right:0;top:0;width:620px;height:508px;background:linear-gradient(120deg,#e7eef4 0%,#c8d6e2 45%,#8fb3d3 75%,#5f95c6 100%)}
.hero-copy{position:absolute;left:112px;top:140px;width:500px}
.hero-copy h1{font-size:56px;font-weight:300;color:var(--ink);margin-bottom:18px}
.hero-copy h1 em{font-style:normal;color:var(--blue);font-weight:400}
.hero-copy p{font-size:15px;line-height:22px;color:var(--text);margin-bottom:30px}
.btn{display:inline-block;font-size:15px;font-weight:500;padding:12px 26px}
.btn-blue{background:var(--blue);color:var(--white)}
.btn-white{background:var(--white);color:var(--ink)}

/* services */
.services{position:absolute;top:700px;left:0;width:1200px;text-align:center}
.services-icon{display:block;margin:0 auto 14px}
.section-title{font-size:26px;font-weight:700;color:var(--blue);text-transform:uppercase}
.title-rule{width:560px;height:1px;background:var(--line);margin:14px auto 0}
.service-cards{position:absolute;top:140px;left:152px;display:flex;gap:4px}
.service-card{width:228px;height:260px;background:var(--white);border:1px solid var(--line);padding-top:26px}
.service-card.featured{background:var(--soft)}
.service-photo{width:120px;height:120px;border-radius:50%;margin:0 auto 18px;background:radial-gradient(circle at 40% 40%,#f2f2f2,#a9b3bb 70%,#7c8690)}
.service-card h3{font-size:18px;font-weight:700;color:var(--ink);text-transform:uppercase;margin-bottom:10px}
.service-card.featured h3{color:var(--blue)}
.service-card p{font-size:12px;line-height:16px;color:var(--text);padding:0 22px;margin-bottom:10px}
.service-card a{font-size:12px;color:var(--blue);font-weight:500}

/* intro */
.intro{position:absolute;top:1150px;left:0;width:1200px;text-align:center}
.intro h2{font-size:30px;font-weight:500;color:var(--ink);text-transform:uppercase;margin-bottom:18px}
.intro p{font-size:26px;line-height:36px;font-weight:300;color:var(--text);width:920px;margin:0 auto}
.intro p b{font-weight:400;color:var(--blue)}

/* panels */
.panels{position:absolute;top:1392px;left:0;width:1200px;height:428px;display:flex}
.panel{width:600px;height:428px;padding:70px 112px 0 112px;color:var(--white)}
.panel-commitment{background:var(--blue-dark);padding-left:112px}
.panel-kiosk{background:linear-gradient(90deg,var(--blue) 0%,var(--blue-light) 100%);padding-left:50px}
.panel h2{font-size:30px;font-weight:700;text-transform:uppercase;margin:14px 0 16px}
.panel p{font-size:14px;line-height:20px;margin-bottom:34px;opacity:.95}

/* testimonial */
.testimonial{position:absolute;top:1820px;left:0;width:1200px;height:440px;background:var(--band);text-align:center}
.testimonial h2{font-size:30px;font-weight:500;color:var(--ink);text-transform:uppercase;padding-top:76px}
.testimonial .title-rule{background:#d2d2d2}
.avatar{width:84px;height:84px;border-radius:50%;margin:28px auto 26px;background:#b9b9b9;border:4px solid var(--white)}
.quote{font-size:19px;line-height:28px;font-style:italic;color:var(--text);width:960px;margin:0 auto 14px}
.quote-author{font-size:15px;color:var(--blue);font-style:italic}
.quote-author span{color:var(--muted)}
.dots{display:flex;gap:8px;justify-content:center;margin-top:18px}
.dots i{width:8px;height:8px;border-radius:50%;background:#9a9a9a}
.dots i.on{background:var(--ink)}

/* map */
.locator{position:absolute;top:2288px;left:0;width:1200px;height:480px}
.map-fill{position:absolute;inset:0;background:linear-gradient(135deg,#e9e4d6 0%,#dde3cf 35%,#cfdcc2 60%,#b9d2e6 100%)}
.locator-form{position:absolute;left:176px;top:20px;width:212px;background:var(--white);box-shadow:0 2px 8px rgba(0,0,0,.25);padding:12px 14px 14px;font-size:13px;color:var(--ink)}
.locator-form label{display:flex;justify-content:space-between;margin-bottom:6px}
.locator-form label a{color:var(--blue);font-size:12px}
.field{height:30px;border:1px solid #ccc;margin-bottom:14px;padding:6px 8px;font-size:13px;display:flex;justify-content:space-between;color:var(--text)}
.locator-form .btn{display:block;text-align:center;padding:8px 0;font-size:13px}
.map-search{position:absolute;left:620px;top:40px;width:410px;background:var(--white);box-shadow:0 2px 6px rgba(0,0,0,.25)}
.map-search .bar{height:36px;border-bottom:1px solid var(--line);display:flex;justify-content:flex-end;align-items:center;padding:0 10px;gap:10px}
.map-search .notice{background:#333;color:var(--white);font-size:12px;padding:8px 12px}

/* footer */
.site-footer{position:absolute;top:2768px;left:0;width:1200px;height:64px;background:var(--footer);color:#bbb;font-size:14px;display:flex;align-items:center;justify-content:space-between;padding:0 40px 0 112px}
.back-top{display:flex;align-items:center;gap:12px;color:var(--white)}
.back-top i{width:40px;height:40px;border-radius:50%;background:var(--white);display:flex;align-items:center;justify-content:center}
</style>
</head>
<body>

<header class="site-header">
  <div class="brand"><span class="brand-square"></span><span class="brand-name">TRAVo</span></div>
  <div class="contact-bar">
    <span><svg width="16" height="12" viewBox="0 0 16 12"><rect x="0.5" y="0.5" width="15" height="11" fill="none" stroke="#1e88d0"/><path d="M1 1l7 6 7-6" fill="none" stroke="#1e88d0"/></svg><b>Email:</b> hello@travo-mail.com</span>
    <span><svg width="12" height="14" viewBox="0 0 12 14"><path d="M2 1h3l1 3-2 1.5a7 7 0 0 0 3.5 3.5L9 7l3 1v3c0 1-1 2-2 2A10 10 0 0 1 0 3c0-1 1-2 2-2z" fill="#1e88d0"/></svg><b>Call us:</b> 555 210 4408</span>
  </div>
  <nav class="main-nav">
    <a href="#" class="active">Home</a><a href="#">About Us</a><a href="#">Services</a><a href="#">Products</a><a href="#">Kiosk</a><a href="#">Contact Us</a>
  </nav>
</header>

<section class="hero">
  <div class="hero-photo" role="img" aria-label="Photo of a young man using a printer at an office kiosk"></div>
  <div class="hero-copy">
    <h1>Welcome to <em>TRAVo</em></h1>
    <p>Lorem ipsum dolor sit amet, consectetur adipiscing elit sed do eiusmod tempor incididunt ut labore et dolore magna aliqua. Ut enim ad minim veniam quis nostrud exercitation ullamco laboris nisi ut aliquip ex ea commodo consequat.</p>
    <a href="#" class="btn btn-blue">Read More</a>
  </div>
</section>

<section class="services">
  <svg class="services-icon" width="40" height="40" viewBox="0 0 40 40"><circle cx="20" cy="20" r="8" fill="none" stroke="#1e88d0" stroke-width="4"/><g stroke="#1e88d0" stroke-width="5" stroke-linecap="round"><path d="M20 3v5M20 32v5M3 20h5M32 20h5M8 8l3.5 3.5M28.5 28.5L32 32M8 32l3.5-3.5M28.5 11.5L32 8"/></g></svg>
  <h2 class="section-title">Our Services</h2>
  <div class="title-rule"></div>
  <div class="service-cards">
    <article class="service-card"><div class="service-photo" role="img" aria-label="Hand holding a tablet"></div><h3>Technology</h3><p>Lorem ipsum dolor sit amet consectetur elit sed do eiusmod tempor incididunt.</p><a href="#">Read More</a></article>
    <article class="service-card featured"><div class="service-photo" role="img" aria-label="Office printer"></div><h3>Printing</h3><p>Lorem ipsum dolor sit amet consectetur elit sed do eiusmod tempor incididunt.</p><a href="#">Read More</a></article>
    <article class="service-card"><div class="service-photo" role="img" aria-label="Flatbed scanner"></div><h3>Scanning</h3><p>Lorem ipsum dolor sit amet consectetur elit sed do eiusmod tempor incididunt.</p><a href="#">Read More</a></article>
    <article class="service-card"><div class="service-photo" role="img" aria-label="Fax machine"></div><h3>Faxing</h3><p>Lorem ipsum dolor sit amet consectetur elit sed do eiusmod tempor incididunt.</p><a href="#">Read More</a></article>
  </div>
</section>

<section class="intro">
  <h2>Mobile Office. Simplified.</h2>
  <p>Where you need it. When you need it. <b>TRAVo Kiosks</b> provide easy access for you to run you mobile office; whether you need to access the internet to research information, access <b>email</b>, <b>download</b> documents or <b>bills</b>.</p>
</section>

<section class="panels">
  <div class="panel panel-commitment">
    <svg width="40" height="32" viewBox="0 0 40 32"><path d="M4 18l8-10 8 6 8-6 8 10-8 8-8-5-8 5z" fill="none" stroke="#fff" stroke-width="3" stroke-linejoin="round"/></svg>
    <h2>Our Commitment</h2>
    <p>Lorem ipsum dolor sit amet, consectetur adipiscing elit sed do eiusmod tempor incididunt ut labore et dolore magna aliqua. Ut enim ad minim veniam, quis nostrud exercitation ullamco laboris nisi ut aliquip ex ea commodo consequat. Duis aute irure dolor in reprehenderit in voluptate velit esse cillum.</p>
    <a href="#" class="btn btn-white">Read More</a>
  </div>
  <div class="panel panel-kiosk">
    <svg width="32" height="32" viewBox="0 0 32 32"><rect x="4" y="2" width="24" height="18" fill="none" stroke="#fff" stroke-width="3"/><path d="M16 20v8M8 30h16" stroke="#fff" stroke-width="3"/></svg>
    <h2>Our Kiosk</h2>
    <p>Lorem ipsum dolor sit amet, consectetur adipiscing elit sed do eiusmod tempor incididunt ut labore et dolore magna aliqua. Ut enim ad minim veniam, quis nostrud exercitation ullamco laboris nisi ut aliquip ex ea commodo consequat. Duis aute irure dolor in reprehenderit in voluptate velit esse cillum.</p>
    <a href="#" class="btn btn-white">Read More</a>
  </div>
</section>

<section class="testimonial">
  <h2>Dana's Testimonial</h2>
  <div class="title-rule"></div>
  <div class="avatar" role="img" aria-label="Portrait of the client"></div>
  <p class="quote">“ Lorem ipsum dolor sit amet, consectetur adipiscing elit, sed do eiusmod tempor incididunt ut labore et dolore magna aliqua nostrud exercitation ullamco laboris nisi ut aliquip ex ea commodo consequat ”</p>
  <p class="quote-author">Dana Reyes <span>| CEO</span></p>
  <div class="dots"><i class="on"></i><i></i><i></i></div>
</section>

<section class="locator">
  <div class="map-fill" role="img" aria-label="Map of kiosk locations across the eastern region"></div>
  <form class="locator-form">
    <label>Find Location <a href="#">Reset</a></label>
    <div class="field">By Region <span>▾</span></div>
    <div class="field">Category <span>▾</span></div>
    <a href="#" class="btn btn-blue">Select</a>
  </form>
  <div class="map-search">
    <div class="bar"><svg width="16" height="16" viewBox="0 0 16 16"><circle cx="6.5" cy="6.5" r="5" fill="none" stroke="#999" stroke-width="2"/><path d="M10 10l5 5" stroke="#999" stroke-width="2"/></svg><svg width="18" height="18" viewBox="0 0 18 18"><circle cx="9" cy="9" r="8" fill="#1e88d0"/><circle cx="9" cy="9" r="3" fill="#fff"/></svg></div>
    <div class="notice">No results found. Try another search nearby.</div>
  </div>
</section>

<footer class="site-footer">
  <span>Copyright © 2015, TRAVo - All rights reserved.</span>
  <a href="#" class="back-top"><i><svg width="14" height="10" viewBox="0 0 14 10"><path d="M1 9l6-7 6 7" fill="none" stroke="#222" stroke-width="2.5"/></svg></i>Back to Top</a>
</footer>

</body>
</html>
```